Modern Design Business Card industrial maintenance company

Business card design for Company named Brookvale Equipment Services

Target Market(s)

Industrial

Industry/Entity Type

Maintenance and repair

Contact Information for Business Card

Place holder for address, office phone, mobile number and email

Requirements
Must have
• Clean modern look
Nice to have
• N/a

```html
<!DOCTYPE html>
<html lang="en">
<head>
<meta charset="utf-8">
<title>Brookvale Equipment Services – Business Card</title>
<link href="https://fonts.googleapis.com/css2?family=Jost:wght@400;500;600&display=swap" rel="stylesheet">
<style>
  :root {
    --page-bg: #e9e6e1;
    --card-black: #050505;
    --ink-white: #f4f4f4;
    --ink-soft: #d9d9d9;
    --ghost: #262626;
    --rule: #8a8a8a;
  }
  * { margin: 0; padding: 0; box-sizing: border-box; }
  html, body { width: 1200px; height: 900px; overflow: hidden; }
  body {
    background: var(--page-bg);
    font-family: "Jost", sans-serif;
    color: var(--ink-white);
    position: relative;
  }
  .card {
    position: absolute;
    left: 320px;
    width: 560px;
    height: 320px;
    background: var(--card-black);
    border-radius: 34px;
    overflow: hidden;
    box-shadow: 0 18px 40px rgba(0,0,0,0.28);
  }
  .card--front { top: 90px; }
  .card--back { top: 480px; }

  /* Front */
  .front-mark {
    position: absolute;
    inset: 0;
    display: flex;
    align-items: center;
    justify-content: center;
    gap: 16px;
  }
  .mark-circle {
    width: 46px; height: 46px;
    border: 3px solid var(--ink-white);
    border-radius: 50%;
    flex: none;
  }
  .brand-name {
    font-weight: 500;
    font-size: 22px;
    letter-spacing: 0.12em;
    text-transform: uppercase;
    color: var(--ink-white);
  }

  /* Back */
  .ghost-circle {
    position: absolute;
    left: 62px; top: 150px;
    width: 230px; height: 230px;
    border: 6px solid var(--ghost);
    border-radius: 50%;
  }
  .person {
    position: absolute;
    left: 34px; top: 44px;
  }
  .person-line {
    display: flex;
    align-items: center;
    gap: 10px;
  }
  .person-name {
    font-weight: 600;
    font-size: 17px;
    letter-spacing: 0.04em;
  }
  .person-sep {
    width: 2px; height: 18px; background: var(--ink-white);
  }
  .person-role { font-size: 14px; color: var(--ink-soft); }
  .contact-row {
    display: flex;
    align-items: center;
    gap: 8px;
    font-size: 13px;
    color: var(--ink-soft);
    margin-top: 6px;
  }
  .contact-row svg { width: 12px; height: 12px; flex: none; }

  .contact-block {
    position: absolute;
    right: 34px; top: 118px;
    width: 250px;
  }
  .contact-block .contact-row { margin-top: 5px; font-size: 12.5px; }
  .contact-rule {
    height: 1px;
    background: var(--rule);
    margin: 12px 0 16px;
  }
  .back-brand {
    display: flex;
    align-items: center;
    gap: 10px;
  }
  .back-brand .mark-circle { width: 40px; height: 40px; }
  .back-brand .brand-name { font-size: 14.5px; letter-spacing: 0.06em; }
</style>
</head>
<body>

<section class="card card--front" aria-label="Card front">
  <div class="front-mark">
    <span class="mark-circle"></span>
    <span class="brand-name">Brookvale Equipment Services</span>
  </div>
</section>

<section class="card card--back" aria-label="Card back">
  <div class="ghost-circle"></div>

  <div class="person">
    <div class="person-line">
      <span class="person-name">JOHN SMITH</span>
      <span class="person-sep"></span>
      <span class="person-role">Director</span>
    </div>
    <div class="contact-row">
      <svg viewBox="0 0 12 12" fill="none" stroke="currentColor" stroke-width="1.2"><rect x="3" y="0.8" width="6" height="10.4" rx="1"/></svg>
      <span>000-000-0000</span>
    </div>
  </div>

  <div class="contact-block">
    <div class="contact-row">
      <svg viewBox="0 0 12 12" fill="currentColor"><path d="M2.5 1l2 2.2-1 1.3c.7 1.5 1.8 2.6 3.3 3.3l1.3-1 2.2 2-1.2 1.7C5 10.4 1.6 7 .8 2.2z"/></svg>
      <span>000-000-0000</span>
    </div>
    <div class="contact-row">
      <svg viewBox="0 0 12 12" fill="currentColor"><path d="M0.5 2.5h11v7h-11z M1 3l5 3.5L11 3" stroke="#050505" stroke-width="0.9"/></svg>
      <span>info@brookvaleservices.com</span>
    </div>
    <div class="contact-row">
      <svg viewBox="0 0 12 12" fill="currentColor"><path d="M6 0.5a3.8 3.8 0 0 0-3.8 3.8C2.2 7 6 11.5 6 11.5S9.8 7 9.8 4.3A3.8 3.8 0 0 0 6 .5zm0 5.2a1.4 1.4 0 1 1 0-2.8 1.4 1.4 0 0 1 0 2.8z"/></svg>
      <span>00 dummy city, dummy place 0000</span>
    </div>
    <div class="contact-rule"></div>
    <div class="back-brand">
      <span class="mark-circle"></span>
      <span class="brand-name">Brookvale Equipment Services</span>
    </div>
  </div>
</section>

</body>
</html>
```